Messestand
Zielgruppe
Wir sind ein Personaldienstleister für Pflegeberufe!
Aufgabenstellung
Überschrift: ...wir PFLEGEN es voraus zu denken!
Anbei finden Sie das Datenblatt für den Messestand!
Zudem finden Sie anbei das Design unserer aktuellen Fahrzeugbeschriftung, welche ich als Designgrundlage gerne auf dem Messestand verwenden würde. Zudem sollte unser Maskottchen "Lotte" darauf zu finden sein! Sowie unser Logo.

```html
<!DOCTYPE html>
<html lang="de">
<head>
<meta charset="utf-8">
<title>Pflegewerk Medical – Messewand</title>
<link href="https://fonts.googleapis.com/css2?family=PT+Sans:wght@400;700&family=PT+Sans+Narrow:wght@400;700&display=swap" rel="stylesheet">
<style>
  :root {
    --stage: #dcdcdc;
    --paper: #ffffff;
    --green: #16a34a;
    --green-deep: #0f8f3f;
    --green-light: #6fcf8f;
    --ink: #1c1c1c;
    --black: #0b0b0b;
    --photo-a: #e6edf2;
    --photo-b: #a9c3d6;
  }
  html, body {
    margin: 0;
    width: 1200px;
    height: 881px;
    overflow: hidden;
    background: var(--stage);
  }
  .wall {
    position: absolute;
    left: 50px;
    top: 60px;
    width: 1100px;
    height: 760px;
    background: var(--paper);
    overflow: hidden;
    box-shadow: 0 6px 18px rgba(0,0,0,0.15);
  }
  .wall-art {
    position: absolute;
    inset: 0;
    width: 1100px;
    height: 760px;
  }
  .brand {
    position: absolute;
    left: 70px;
    top: 50px;
    display: flex;
    align-items: center;
    gap: 22px;
  }
  .brand-dot {
    width: 126px;
    height: 126px;
    border-radius: 50%;
    background: var(--green);
  }
  .brand-name {
    font-family: "PT Sans Narrow", "PT Sans", sans-serif;
    font-weight: 400;
    font-size: 52px;
    letter-spacing: 1px;
    color: var(--green);
    margin-top: 20px;
  }
  .headline {
    position: absolute;
    left: 93px;
    top: 358px;
    margin: 0;
    font-family: "PT Sans", sans-serif;
    font-weight: 700;
    font-size: 41px;
    line-height: 56px;
    letter-spacing: 1px;
    color: var(--ink);
    text-transform: uppercase;
  }
  .headline .accent { color: var(--paper); }
  .web {
    position: absolute;
    left: 90px;
    top: 668px;
    font-family: "PT Sans", sans-serif;
    font-size: 25px;
    color: var(--paper);
  }
</style>
</head>
<body>
  <main class="wall">
    <svg class="wall-art" viewBox="0 0 1100 760" xmlns="http://www.w3.org/2000/svg">
      <defs>
        <linearGradient id="photoTone" x1="0" y1="0" x2="1" y2="1">
          <stop offset="0" stop-color="var(--photo-a)"/>
          <stop offset="1" stop-color="var(--photo-b)"/>
        </linearGradient>
        <linearGradient id="dotTone" x1="0" y1="0" x2="1" y2="0">
          <stop offset="0" stop-color="#ffffff"/>
          <stop offset="0.5" stop-color="#8fd8a8"/>
          <stop offset="1" stop-color="#d8f2e0"/>
        </linearGradient>
        <radialGradient id="greenGlow" cx="0.28" cy="0.2" r="0.5">
          <stop offset="0" stop-color="var(--green-light)"/>
          <stop offset="1" stop-color="var(--green)"/>
        </radialGradient>
      </defs>

      <rect class="halftone-field" x="560" y="330" width="540" height="430" fill="url(#dotTone)" role="img" aria-label="Grünes Punkteraster, nach rechts auslaufend"/>

      <path class="green-wave" fill="url(#greenGlow)"
        d="M0,250 C220,190 420,250 580,320 C750,395 950,405 1100,300 L1100,345 C990,430 800,420 630,372 L560,352 L560,760 L0,760 Z"/>

      <path class="black-swoosh" fill="var(--black)"
        d="M600,360 C780,430 960,440 1100,345 L1100,380 C960,480 760,455 600,368 Z"/>

      <path class="green-arc" fill="var(--green)"
        d="M545,90 C570,40 620,12 670,5 L720,0 C650,20 590,60 560,130 Z"/>

      <ellipse class="team-photo" cx="830" cy="180" rx="300" ry="170" transform="rotate(-12 830 180)"
        fill="url(#photoTone)" role="img" aria-label="Foto: lächelndes Pflegeteam in Dienstkleidung, vorne eine Pflegekraft mit Stethoskop"/>

      <path class="base-band" fill="var(--black)"
        d="M0,620 C170,555 420,575 560,760 L0,760 Z"/>
    </svg>

    <div class="brand">
      <span class="brand-dot"></span>
      <span class="brand-name">PFLEGEWERK MEDICAL</span>
    </div>

    <h1 class="headline">Wir <span class="accent">pflegen</span> es<br>voraus zu denken.</h1>

    <div class="web">www.pflegewerk-team.de</div>
  </main>
</body>
</html>
```